Ripple (nightclub flyer)

Nightclub flyer, guaranteed project. Text below (and please use logos, large):

RIPPLE PRESENTS:

KORVEN (LOGO) B2B MARTIN VOLKE (LOGO)

+TREVV LANE (smaller text)

10/26/17

2284 HARLOW AVENUE SACRAMENTO CA
21+ 10PM-2AM

HOUSE/TECHNO

A BLUE CASCADE ENTERTAINMENT (LOGO) PRODUCTION

Target Market(s)

House/Electronic Music Lovers

Industry/Entity Type

Night Club

Font styles to use
Sans Serif

Colors

Designer to choose colors to be used in the design.

Requirements
Must have
• Large logos for the dj names, or large block letter dj names (logos not necessary if it looks better without. But KORVEN b2b MARTIN VOLKE large and TREVV LANE smaller on separate line
Nice to have
• Can include a classy female model but nothing cheesy or too sexy

```html
<!DOCTYPE html>
<html lang="en">
<head>
<meta charset="utf-8">
<title>Ripple Presents — Korven B2B Martin Volke</title>
<link rel="stylesheet" href="https://fonts.googleapis.com/css2?family=Anton&family=Orbitron:wght@400;500;700&display=swap">
<style>
  :root {
    --stage: #dcdcdc;
    --night-deep: #070a3a;
    --night-blue: #1b2fb8;
    --night-violet: #6a1fb0;
    --night-magenta: #c21ea8;
    --neon-cyan: #5fd8ff;
    --neon-pink: #ff4d9a;
    --neon-yellow: #f4f08a;
    --ice: #cfefff;
    --gold-light: #f3dc8c;
    --gold-dark: #b8913a;
    --silver-light: #ffffff;
    --silver-mid: #c9ccd4;
    --silver-dark: #8a8f99;
    --caption: #e8ecff;
  }
  * { margin: 0; padding: 0; box-sizing: border-box; }
  html, body { width: 1200px; height: 800px; overflow: hidden; }
  body {
    background: radial-gradient(ellipse at center, #ececec 0%, var(--stage) 70%, #cfcfcf 100%);
    position: relative;
    font-family: "Orbitron", sans-serif;
  }
  .flyer {
    position: absolute;
    left: 325px; top: 37px;
    width: 572px; height: 740px;
    overflow: hidden;
    background:
      radial-gradient(ellipse 45% 32% at 50% 44%, rgba(194,30,168,.85) 0%, rgba(106,31,176,.55) 45%, transparent 75%),
      radial-gradient(ellipse 40% 30% at 8% 35%, rgba(40,110,255,.6) 0%, transparent 70%),
      radial-gradient(ellipse 60% 40% at 90% 15%, rgba(120,40,200,.6) 0%, transparent 70%),
      linear-gradient(180deg, #1a1c8c 0%, var(--night-blue) 30%, #2a1fa0 55%, #121670 78%, var(--night-deep) 100%);
  }
  .flyer-lines { position: absolute; inset: 0; width: 100%; height: 100%; }
  .centered { position: absolute; left: 0; width: 100%; text-align: center; }
  .presenter {
    top: 100px;
  }
  .presenter span {
    display: inline-block;
    font-size: 15px; font-weight: 500; letter-spacing: 1px;
    color: var(--neon-cyan);
    border: 1.5px solid var(--neon-cyan);
    padding: 1px 5px 0;
  }
  .headliner {
    font-family: "Anton", sans-serif;
    text-transform: uppercase;
    line-height: 1;
    background: linear-gradient(180deg, var(--silver-light) 0%, var(--silver-mid) 45%, var(--silver-dark) 55%, var(--silver-light) 100%);
    -webkit-background-clip: text; background-clip: text;
    color: transparent;
    filter: drop-shadow(0 2px 3px rgba(0,0,0,.55));
  }
  .headliner--first { top: 184px; font-size: 96px; letter-spacing: 1px; }
  .headliner--b2b { top: 294px; font-size: 52px; }
  .headliner--second { top: 350px; font-size: 88px; letter-spacing: 1px; }
  .support {
    top: 447px;
    font-family: "Anton", sans-serif;
    font-size: 32px; letter-spacing: 1px;
    background: linear-gradient(180deg, var(--gold-light) 0%, var(--gold-dark) 100%);
    -webkit-background-clip: text; background-clip: text;
    color: transparent;
  }
  .event-date {
    top: 508px;
    font-size: 50px; font-weight: 400; letter-spacing: 2px;
    color: var(--ice);
    text-shadow: 0 0 8px rgba(95,216,255,.9), 0 0 18px rgba(95,216,255,.5);
  }
  .venue {
    top: 572px;
    font-size: 12px; font-weight: 500; letter-spacing: .5px; line-height: 16px;
    color: var(--caption);
  }
  .credit-line {
    top: 664px;
    font-size: 8px; font-weight: 500; letter-spacing: .5px;
    color: var(--caption);
  }
  .producer-name {
    top: 690px;
    display: flex; justify-content: center; align-items: center; gap: 6px;
    font-size: 12px; font-weight: 700; letter-spacing: 1px;
    color: var(--silver-mid);
  }
  .producer-name i {
    display: inline-block; width: 14px; height: 14px; border-radius: 50%;
    background: var(--silver-mid);
  }
  .credit-tail {
    top: 724px;
    font-size: 8px; font-weight: 500; letter-spacing: .5px;
    color: var(--caption);
  }
</style>
</head>
<body>
  <main class="flyer">
    <svg class="flyer-lines" viewBox="0 0 572 740" aria-hidden="true">
      <defs>
        <linearGradient id="tri-warm" x1="0" y1="0" x2="1" y2="1">
          <stop offset="0" stop-color="#ff4d9a"/>
          <stop offset="0.6" stop-color="#ff8ac0"/>
          <stop offset="1" stop-color="#5fd8ff"/>
        </linearGradient>
        <linearGradient id="tri-cool" x1="0" y1="0" x2="1" y2="1">
          <stop offset="0" stop-color="#5fd8ff"/>
          <stop offset="0.7" stop-color="#9ff0ff"/>
          <stop offset="1" stop-color="#f4f08a"/>
        </linearGradient>
        <filter id="glow" x="-20%" y="-20%" width="140%" height="140%">
          <feGaussianBlur stdDeviation="2.5" result="b"/>
          <feMerge><feMergeNode in="b"/><feMergeNode in="SourceGraphic"/></feMerge>
        </filter>
      </defs>
      <g stroke="#7fb0ff" stroke-opacity=".25" stroke-width="1" fill="none">
        <line x1="0" y1="300" x2="572" y2="60"/>
        <line x1="0" y1="520" x2="572" y2="250"/>
        <line x1="120" y1="0" x2="300" y2="740"/>
        <line x1="430" y1="0" x2="260" y2="740"/>
      </g>
      <polygon points="286,40 50,178 50,470 286,610 522,470 522,178"
               fill="none" stroke="#8fb4ff" stroke-opacity=".45" stroke-width="1.2"/>
      <g filter="url(#glow)" fill="none" stroke-width="2.2">
        <polygon points="85,238 435,190 375,458" stroke="url(#tri-warm)"/>
        <polygon points="280,133 115,480 390,520" stroke="url(#tri-cool)"/>
      </g>
    </svg>

    <p class="centered presenter"><span>RIPPLE PRESENTS</span></p>
    <h1 class="centered headliner headliner--first">Korven</h1>
    <p class="centered headliner headliner--b2b">B2B</p>
    <h1 class="centered headliner headliner--second">Martin Volke</h1>
    <p class="centered support">+ TREVV LANE</p>
    <p class="centered event-date">10.26.17</p>
    <p class="centered venue">2284 HARLOW AVENUE SACRAMENTO CA<br>21+ 10PM-2AM</p>
    <p class="centered credit-line">A BLUE CASCADE ENTERTAINMENT</p>
    <p class="centered producer-name"><i></i>BLUE CASCADE</p>
    <p class="centered credit-tail">PRODUCTIONS</p>
  </main>
</body>
</html>
```